Book cover design for a collection of poetry - The Lanternfield

Book cover and back design need to be moody, nostalgic, reflective, ethereal. Melancholy and other worldly. Cover design should not be time specific to a period or place but if applicable should reflect British landscape. Book cover should be in tones of blue and must include the title and author (THE LANTERNFIELD BY DORIAN WELKBRIDGE). We love the idea of rain, and looking out of a window. See attached designs. A world you are observing but not in.

Industry/Entity Type

Book Publisher

Font styles to use
Serif
Script

Colors
3176b5
3377b5
85acd3
eaf1f7
0792cd
33a6d7
86cae7
ecf7fb
86cfc6

Requirements
Must have
• The colour blue in it, must be melancholy and reflective.
Nice to have
• Rain in the cover.
Should not have
• Any bright colours.

```html
<!DOCTYPE html>
<html lang="en">
<head>
<meta charset="utf-8">
<title>The Lanternfield — Dorian Welkbridge</title>
<link href="https://fonts.googleapis.com/css2?family=Merriweather:wght@400&display=swap" rel="stylesheet">
<style>
  :root {
    --night-navy: #141a48;
    --window-blue: #00b1e6;
    --window-blue-deep: #00a6dc;
    --rain-light: #b9dcf5;
    --paper-white: #ffffff;
  }
  * { margin: 0; padding: 0; box-sizing: border-box; }
  html, body {
    width: 800px;
    height: 1200px;
    overflow: hidden;
    background: var(--night-navy);
  }
  .cover {
    position: relative;
    width: 800px;
    height: 1200px;
    background: var(--night-navy);
    font-family: "Merriweather", Georgia, serif;
    color: var(--paper-white);
  }
  .rain-window {
    position: absolute;
    left: 0;
    top: 0;
    width: 800px;
    height: 1200px;
  }
  .title {
    font-weight: 400;
    font-size: inherit;
  }
  .title-line {
    position: absolute;
    left: 0;
    width: 800px;
    text-align: center;
    font-weight: 400;
    font-size: 90px;
    line-height: 1;
    letter-spacing: -0.5px;
    white-space: nowrap;
  }
  .title-line--first { top: 743px; }
  .title-line--second { top: 847px; }
  .author {
    position: absolute;
    left: 0;
    top: 1079px;
    width: 800px;
    text-align: center;
    font-weight: 400;
    font-size: 40px;
    line-height: 1;
    white-space: nowrap;
  }
</style>
</head>
<body>
  <main class="cover">
    <svg class="rain-window" viewBox="0 0 800 1200" xmlns="http://www.w3.org/2000/svg">
      <defs>
        <radialGradient id="rainGlow" cx="0.55" cy="0.4" r="0.7">
          <stop offset="0" stop-color="#3cbfeb"/>
          <stop offset="0.6" stop-color="#00b1e6"/>
          <stop offset="1" stop-color="#00a6dc"/>
        </radialGradient>
      </defs>
      <polygon role="img" aria-label="Rain-covered window pane with water droplets on blue glass"
               points="114,148 684,148 582,599 209,599" fill="url(#rainGlow)"/>
    </svg>
    <h1 class="title">
      <span class="title-line title-line--first">The</span>
      <span class="title-line title-line--second">Lanternfield</span>
    </h1>
    <p class="author">Dorian Welkbridge</p>
  </main>
</body>
</html>
```